I need a book cover for Lenni who was born in the early 1900s.

Lenni braved a difficult life when she became a "mother" (at age 13) to her brothers and sisters.

Her mother died of the influenza.

There was no running water from faucets (water was drawn from windmills), electricity, or gas.

There were wood‐burning iron stoves and pot‐belly heaters, and the firewood had to be found and carried home in horse‐drawn wagons, chopped, and then carried into the home.

The final design should show how Lenni, children, and grandchildren advanced from a 3rd grade education to Ph.D. status.

Target Market(s)

Families

Industry/Entity Type

Education

Font styles to use
Serif
Script

Colors
f9a040

Requirements
Must have
• Cover: Picture of young Lenni (see example cover attached)
OR
Picture of Lenni (older) maroon suit
Title: Radiant Lenni
Words: At 13, Lenni raised the orphaned family, when her mother died.
Orange background (attached)
Nice to have
• Pictures across of old tools of the past (old stove, iron, lantern, wagon) (see example cover attached)
OR
Orange sky with sun and windmill picture (attached)
Should not have
• The design should not use old-style, serif fonts like Times New Roman.

```html
<!DOCTYPE html>
<html lang="en">
<head>
<meta charset="utf-8">
<title>Radiant Lenni – Book Cover</title>
<link rel="stylesheet" href="https://fonts.googleapis.com/css2?family=Great+Vibes&family=Arimo:wght@400;700&family=Roboto+Condensed:wght@700&family=Oswald:wght@600&display=swap">
<style>
  :root {
    --stage: #e9e6e2;
    --sky-top: #b5561c;
    --sky-mid: #f9a040;
    --sky-glow: #f6c35c;
    --sky-low: #c9661f;
    --earth: #7a3515;
    --back-top: #9c3f1a;
    --back-bottom: #6e2a12;
    --ink: #160c06;
    --cream: #fde7c0;
    --white: #ffffff;
    --portrait-dark: #3a1f12;
    --portrait-mid: #8a5a3a;
  }
  * { margin: 0; padding: 0; box-sizing: border-box; }
  html, body { width: 1200px; height: 900px; overflow: hidden; background: var(--stage); }
  .canvas { position: relative; width: 1200px; height: 900px; }

  .book { position: absolute; left: 195px; top: 150px; display: flex; height: 600px; box-shadow: 0 10px 30px rgba(0,0,0,.25); }

  /* Back cover */
  .back-cover {
    position: relative; width: 380px; height: 600px; padding: 36px 28px 28px 26px;
    background: linear-gradient(180deg, var(--back-top) 0%, #b45a22 45%, var(--back-bottom) 100%);
    color: var(--white); font-family: "Arimo", Arial, sans-serif; font-size: 9.6px; line-height: 1.72;
  }
  .back-cover .sky-band {
    position: absolute; left: 0; right: 0; top: 300px; height: 70px;
    background: linear-gradient(180deg, transparent, rgba(246,195,92,.55), transparent);
  }
  .back-copy { position: relative; width: 300px; }
  .back-copy p { margin-bottom: 11px; }
  .back-copy .heading { font-weight: 700; margin-bottom: 0; }

  /* Spine */
  .spine {
    position: relative; width: 50px; height: 600px;
    background: linear-gradient(180deg, var(--sky-top), var(--sky-mid) 45%, var(--sky-low) 100%);
    border-left: 1px solid rgba(0,0,0,.25); border-right: 1px solid rgba(0,0,0,.2);
  }
  .spine-title {
    position: absolute; left: 50%; top: 40px; transform-origin: left top;
    transform: rotate(90deg) translate(0, -50%);
    font-family: "Great Vibes", cursive; font-size: 42px; color: var(--ink); white-space: nowrap;
  }

  /* Front cover */
  .front-cover { position: relative; width: 380px; height: 600px; overflow: hidden; }
  .front-sky {
    position: absolute; inset: 0;
    background:
      radial-gradient(ellipse 60% 18% at 55% 42%, var(--sky-glow), transparent 70%),
      linear-gradient(180deg, var(--sky-top) 0%, var(--sky-mid) 35%, #f2a23e 48%, var(--sky-low) 75%, var(--earth) 100%);
  }
  .sun-art {
    position: absolute; right: 42px; top: 248px; width: 90px; height: 52px;
    border-radius: 45px 45px 0 0; background: rgba(253,231,192,.55);
  }
  .wheel-art {
    position: absolute; right: 14px; top: 380px; width: 130px; height: 150px;
    background: radial-gradient(ellipse at 50% 50%, rgba(90,40,15,.45), transparent 70%);
  }
  .author {
    position: absolute; right: 22px; top: 30px;
    font-family: "Oswald", sans-serif; font-weight: 600; font-size: 22px; color: var(--cream);
  }
  .title {
    position: absolute; left: 48px; top: 88px;
    font-family: "Great Vibes", cursive; font-weight: 400; font-size: 56px; color: var(--ink); line-height: 1;
  }
  .tagline {
    position: absolute; left: 82px; top: 144px;
    font-family: "Arimo", Arial, sans-serif; font-style: italic; font-size: 11.5px; color: var(--ink);
  }
  .portrait {
    position: absolute; left: 60px; top: 250px; width: 200px; height: 300px;
    border-radius: 90px 90px 0 0;
    background: linear-gradient(180deg, var(--portrait-dark) 0%, var(--portrait-mid) 40%, var(--portrait-dark) 75%, #1e0f08 100%);
    opacity: .9;
  }
  .cover-line {
    position: absolute; left: 0; right: 0; bottom: 24px; text-align: center;
    font-family: "Roboto Condensed", sans-serif; font-weight: 700; font-size: 15.5px; color: var(--white);
  }
</style>
</head>
<body>
<main class="canvas">
  <div class="book">
    <section class="back-cover">
      <div class="sky-band" role="img" aria-label="Sunset sky with faded windmill and old farm tools"></div>
      <div class="back-copy">
        <p class="heading">Lenni—Radiant Grandma</p>
        <p>Narrated by: Lenora T. Olvera</p>
        <p>Author: Marisa Olvera<br>© by the author of this book. The book author retains sole copyright to her contributions to this e-book.</p>
        <p>LENORA T. OLVERA<br>1904-2002</p>
        <p>- Born December 14th, 1904.<br>- Born in Las Piedras, New Mexico.<br>- Mother, filled in as father (widowed), mother-in-law, grandmother, great-grandmother, adopted grandmother, nurse, nanny, maid, field hand, horse rider, chief cook and bottle washer, seamstress, teacher, advisor, community leader, navigator of the family, baker, hair dresser, and other jobs, always.<br>- Sadly left us on August 28th, 2002, at age 97.</p>
        <p>Stricken with the unusually deadly influenza pandemic, Grandma's mother, Celestina Ortega Ruiz, age 36, and 6-month-old son passed on.</p>
        <p class="heading">Lifestyle Change</p>
        <p>At 13 years of age, Grandma's lifestyle changed drastically. Never having heard a kind word, a hug, or kiss for Grandma before, her father promptly took her away from her grandparents' home, so that she could assist with the orphaned children. Grandma learned to tend the family who were her father, one older brother, two younger sisters, and two younger brothers who were only 2 and 4 years old. Grandma says she already knew how to cook beans, prepare chile, and make tortillas, and she quickly learned how to do everything else.</p>
      </div>
    </section>

    <div class="spine">
      <span class="spine-title">Radiant Lenni</span>
    </div>

    <section class="front-cover">
      <div class="front-sky" role="img" aria-label="Orange sunset sky with glowing clouds over the plains"></div>
      <div class="sun-art" role="img" aria-label="Rising sun illustration"></div>
      <div class="wheel-art" role="img" aria-label="Old wagon wheel drawing with a small bird"></div>
      <div class="author">Marisa Olvera</div>
      <h1 class="title">Radiant Lenni</h1>
      <p class="tagline">"Face Everything Avoid Nothing"</p>
      <div class="portrait" role="img" aria-label="Portrait photograph of Lenni as an older woman in a dark suit and pearl necklace"></div>
      <p class="cover-line">At 13, Lenni raised the orphaned family, when her mother died</p>
    </section>
  </div>
</main>
</body>
</html>
```